Bref créative
Letterhead, envelope, business card design
Marlowe Crest Advisory
I need double sided standard sized Business Card [3.5" x 2"]
Use whatever font you think is best
Professional
R. Dwight Folsom, DWMA®
Wealth Advisor
2400 Birchmoor Avenue
Suite 418
Delford, PA 19586
rfolsom@marlowe-crest.example
www.marlowe-crest.example
The following disclosure goes on letterhead at the bottom, on the back of the envelope on the flap, and on the business card.
Securities offered through QVD Brokerage, Member NAXO/BTPE.
Investment advice offered through Harbor Counsel Partners, a registered investment advisor.
Harbor Counsel Partners and Marlowe Crest Advisory are separate entities from QVD Brokerage.
You can either design a one sided business card or a two sided business card. If you design a two sided card, follow these guidelines:
1. Place the address on the back of the card along with the disclosure. Logo, name and title can remain on the front side of the card. OR
2. Place the disclosure on the front of the card and move “nonessential” information such as website address, fax number, etc. to the back.
Existing logo files

```html
<!DOCTYPE html>
<html lang="en">
<head>
<meta charset="utf-8">
<title>Marlowe Crest Advisory – Stationery</title>
<link href="https://fonts.googleapis.com/css2?family=Cinzel:wght@600&family=Lato:wght@400;700&display=swap" rel="stylesheet">
<style>
:root{
  --navy:#1d3a6a;
  --navy-deep:#142a4f;
  --gold:#c9a33d;
  --paper:#ffffff;
  --ink:#34425a;
  --muted:#8a93a3;
  --stage-dark:#2e2f33;
  --stage-light:#8b8d91;
  --label:#d4d6da;
}
*{margin:0;padding:0;box-sizing:border-box}
html,body{width:1200px;height:500px;overflow:hidden}
body{
  position:relative;
  background:radial-gradient(ellipse at 50% 45%,var(--stage-light) 0%,#606266 55%,var(--stage-dark) 100%);
  font-family:'Lato',sans-serif;color:var(--ink);
}
.piece{position:absolute;box-shadow:0 3px 8px rgba(0,0,0,.45)}
.label{position:absolute;font-size:7px;color:var(--label);text-align:center;width:187px}
.card{width:187px;height:91px;overflow:hidden}
.card--navy{background:linear-gradient(160deg,var(--navy) 0%,var(--navy-deep) 100%);color:#fff}
.card--white{background:var(--paper);border-right:4px solid var(--navy)}
.wordmark{font-family:'Cinzel',serif;font-weight:600;letter-spacing:.06em;line-height:1.05}
.mark{display:inline-block;border-radius:50%;background:var(--gold)}
.brand{display:flex;align-items:center;gap:6px}
.card .rule{position:absolute;height:1px;background:var(--gold)}
.fine{font-size:3.4px;line-height:1.35;text-align:center}
.contact{font-size:5.2px;line-height:1.6}
.contact b{font-weight:700;font-size:6px;color:var(--navy)}
.center{position:absolute;left:0;right:0;display:flex;flex-direction:column;align-items:center}
.letterhead{left:434px;top:22px;width:322px;height:458px;background:var(--paper);border-left:7px solid var(--navy)}
.envelope{background:var(--paper);width:403px}
</style>
</head>
<body>

<!-- Business cards: option 1 -->
<div class="piece card card--navy" style="left:29px;top:89px">
  <div class="center" style="top:22px">
    <div class="brand"><span class="mark" style="width:11px;height:11px"></span>
      <div class="wordmark" style="font-size:11px;color:#fff">Marlowe Crest<br><span style="font-size:7px;color:var(--gold)">Advisory</span></div></div>
  </div>
  <div class="rule" style="left:20px;right:20px;top:62px"></div>
  <div class="center fine" style="top:67px;color:#c9d3e4">2400 Birchmoor Avenue · Suite 418 · Delford, PA 19586<br>Securities offered through QVD Brokerage, Member NAXO/BTPE.</div>
</div>
<div class="label" style="left:29px;top:183px">Back Card Option #1</div>

<div class="piece card card--white" style="left:216px;top:89px;left:222px">
  <div style="position:absolute;left:10px;top:12px" class="contact">
    <b>R. Dwight Folsom, DWMA®</b><br>Wealth Advisor<br>
    <span style="color:var(--muted)">✉ rfolsom@marlowe-crest.example<br>◉ www.marlowe-crest.example</span>
  </div>
  <div class="brand" style="position:absolute;right:10px;bottom:12px"><span class="mark" style="width:8px;height:8px"></span>
    <div class="wordmark" style="font-size:8px;color:var(--navy)">Marlowe Crest<br><span style="font-size:5px">Advisory</span></div></div>
</div>
<div class="label" style="left:222px;top:183px">Front Card Option #1</div>

<!-- option 2 -->
<div class="piece card card--navy" style="left:29px;top:211px">
  <div class="center" style="top:16px">
    <span class="mark" style="width:30px;height:30px;background:#fff"></span>
    <div class="wordmark" style="font-size:7px;margin-top:6px;color:#fff">Marlowe Crest Advisory</div>
    <div style="font-size:4.5px;margin-top:5px;color:#c9d3e4">www.marlowe-crest.example</div>
  </div>
</div>
<div class="label" style="left:29px;top:307px">Back Card Option #2</div>

<div class="piece card card--white" style="left:222px;top:211px">
  <div class="brand" style="position:absolute;right:12px;top:10px"><span class="mark" style="width:10px;height:10px"></span>
    <div class="wordmark" style="font-size:9px;color:var(--navy)">Marlowe Crest<br><span style="font-size:6px">Advisory</span></div></div>
  <div style="position:absolute;left:10px;top:46px" class="contact">
    <b>R. Dwight Folsom, DWMA®</b><br>Wealth Advisor<br>
    <span style="color:var(--muted)">2400 Birchmoor Avenue, Suite 418<br>Delford, PA 19586</span>
  </div>
  <div style="position:absolute;right:10px;top:52px;text-align:right;color:var(--muted)" class="contact">rfolsom@marlowe-crest.example<br>www.marlowe-crest.example</div>
</div>
<div class="label" style="left:222px;top:307px">Front Card Option #2</div>

<!-- option 3 & 4 -->
<div class="piece card card--navy" style="left:29px;top:346px">
  <div class="center" style="top:14px">
    <span class="mark" style="width:34px;height:34px;background:#fff"></span>
    <div style="font-size:4.5px;margin-top:8px;color:#c9d3e4">www.marlowe-crest.example</div>
  </div>
</div>
<div class="label" style="left:29px;top:441px">Back Card Option #3</div>

<div class="piece card card--navy" style="left:222px;top:346px">
  <div class="center" style="top:14px">
    <span class="mark" style="width:34px;height:34px"></span>
    <div style="font-size:4.5px;margin-top:8px;color:#c9d3e4">www.marlowe-crest.example</div>
  </div>
</div>
<div class="label" style="left:222px;top:441px">Back Card Option #4</div>

<!-- Letterhead -->
<div class="piece letterhead">
  <div class="brand" style="position:absolute;left:18px;top:18px"><span class="mark" style="width:16px;height:16px"></span>
    <div class="wordmark" style="font-size:14px;color:var(--navy)">Marlowe Crest<br><span style="font-size:9px">Advisory</span></div></div>
  <div class="contact" style="position:absolute;right:16px;top:16px;font-size:5px;color:var(--muted)">
    2400 Birchmoor Avenue · Suite 418<br>Delford, PA 19586<br>www.marlowe-crest.example
  </div>
  <div class="fine" style="position:absolute;left:20px;right:20px;bottom:16px;font-size:4px;color:var(--muted)">
    Securities offered through QVD Brokerage, Member NAXO/BTPE.<br>
    Investment advice offered through Harbor Counsel Partners, a registered investment advisor.<br>
    Harbor Counsel Partners and Marlowe Crest Advisory are separate entities from QVD Brokerage.
  </div>
</div>
<div class="label" style="left:502px;top:483px">Letterhead Option #1</div>

<!-- Envelope back -->
<div class="piece envelope" style="left:773px;top:65px;height:187px">
  <svg width="403" height="187" viewBox="0 0 403 187" style="position:absolute;inset:0">
    <polyline points="0,0 201,82 403,0" fill="none" stroke="#cfd3da" stroke-width="1"/>
    <polyline points="0,187 150,92" fill="none" stroke="#e1e4e9" stroke-width="1"/>
    <polyline points="403,187 252,92" fill="none" stroke="#e1e4e9" stroke-width="1"/>
  </svg>
  <div class="fine" style="position:absolute;left:90px;right:90px;top:14px;font-size:4px;color:var(--muted)">
    Securities offered through QVD Brokerage, Member NAXO/BTPE.<br>
    Investment advice offered through Harbor Counsel Partners, a registered investment advisor.<br>
    Harbor Counsel Partners and Marlowe Crest Advisory are separate entities from QVD Brokerage.
  </div>
  <div class="center" style="top:96px">
    <div class="brand"><span class="mark" style="width:10px;height:10px"></span>
      <div class="wordmark" style="font-size:8px;color:var(--navy)">Marlowe Crest Advisory</div></div>
    <div class="fine" style="font-size:4px;margin-top:6px;color:var(--muted)">2400 Birchmoor Avenue · Suite 418 · Delford, PA 19586</div>
  </div>
</div>

<!-- Envelope front -->
<div class="piece envelope" style="left:773px;top:317px;height:163px;border-left:6px solid var(--navy)">
  <div class="brand" style="position:absolute;left:12px;top:12px"><span class="mark" style="width:12px;height:12px"></span>
    <div class="wordmark" style="font-size:11px;color:var(--navy)">Marlowe Crest<br><span style="font-size:7px">Advisory</span></div></div>
  <div class="contact" style="position:absolute;left:14px;top:42px;font-size:4.6px;color:var(--muted)">2400 Birchmoor Avenue, Suite 418<br>Delford, PA 19586</div>
</div>
<div class="label" style="left:880px;top:255px">Envelope Front &amp; Back</div>

</body>
</html>
```